Fatigued and Overloaded by COVID Messages? We need original illustrations to show that.

Everywhere you look there are messages about COVID. That is leading many people to feel fatigued and overloaded by the messages.

We surveyed U.S. adults March 20th - 24th, 2020 and measured message fatigue, information overload, perceived repetition, and perceived exaggeration. Here is how participants responded:

When it comes to coronavirus . . .
55% feel exhausted by all the messages.
54% feel overloaded by the amount of information.
51% feel that the messages are repetitive.
47% feel like messages exaggerate how bad it is.

In other words, almost half of U.S. adults show signs of message fatigue, information overload, perceived message repetition, and perceived message exaggeration.

We will continue to survey 400 adults every week for the next 16 weeks. Each time we will measure message fatigue, information overload, perceived repetition, and perceived exaggeration. We expect that it will increase over time.

What are we looking for? We need innovative and original illustrations that attempt to communicate these findings. The illustrations would visualize message fatigue, information overload, perceived message repetition, and perceived message exaggeration.

What sort of visual are we looking for? Our preference is for an original illustration (or set of illustrations). Our preference is for creative and powerful illustrations, but we are also open to the creative and well-executed infographics.

We need these images fast . We will award monetary prizes to the 3 best designs. If we like more than that, then we might purchase more (e.g., in past contests, we have purchased as many as 30 designs).

What we will need:
(1) The illustrations must be original and we will need the photoshop and/or illustrator files for all artwork. (By original, we mean that the illustrations are 100% created by you. Our organization requires that we utilize only original illustrated work. We have had issues with free imagery being pirated and reposted as free. We sidestep that issue by just having everything created.)

(2) The illustration should say, somewhere: "Based on a survey of 400 U.S. adults conducted March 20 - 24th, 2020."

(3) We will have almost 4 months worth of data by the time this is done. In other words, the illustrations might be able to help us present that weekly data.

(4) We have conducted other Artvendo projects. It might be helpful to examine designs we liked in the past. For example, here is another COVID project we just finished:

https://jobs.artvendo-example.com/job/5162048

Target Market(s)

U.S. adults

Requirements
Must have
• Original illustrations. Mobile friendly design. People will view this on their smartphones.
Nice to have
• A design that we can use to communicate the data across time.

```html
<!DOCTYPE html>
<html lang="en">
<head>
<meta charset="utf-8">
<title>COVID Message Fatigue – Week 1</title>
<link rel="stylesheet" href="https://fonts.googleapis.com/css2?family=Nunito+Sans:wght@300;400;800;900&family=Arimo:wght@400&display=swap">
<style>
  :root {
    --white: #ffffff;
    --ink: #1a1a1a;
    --ink-soft: #3a3a3a;
    --sky-deep: #5f8fcf;
    --sky-light: #8fc8ff;
    --virus-core: #ffd21a;
    --virus-mid: #ff6a10;
    --virus-edge: #f2231a;
    --skin: #f7c48a;
    --mask-teal: #9fd4c4;
    --flag-red: #b3121c;
    --sun-yellow: #fcc200;
    --bar-empty: #000000;
    --red: #f20d12;
    --green: #006a38;
    --indigo: #2b16b4;
    --steel: #5c8ccf;
    --virus-orange: #ff9200;
    --virus-sage: #d4e0c0;
    --divider: #d8b64a;
  }
  * { box-sizing: border-box; margin: 0; padding: 0; }
  html, body { width: 1200px; height: 2438px; overflow: hidden; background: var(--white); }
  body { position: relative; font-family: "Nunito Sans", sans-serif; color: var(--ink); }

  .page-title {
    position: absolute; top: 0; left: 0; width: 1200px; height: 99px;
    display: flex; align-items: center; justify-content: center;
    font-weight: 900; font-size: 43px; letter-spacing: 0.6px;
  }
  .hero-art {
    position: absolute; top: 99px; left: 0; width: 1200px; height: 895px;
    background:
      radial-gradient(ellipse 300px 300px at 407px 374px, var(--virus-core) 0%, var(--virus-mid) 35%, var(--virus-edge) 70%, rgba(242,35,26,0) 100%),
      radial-gradient(ellipse 260px 300px at 1120px 820px, var(--flag-red) 0%, var(--skin) 40%, var(--mask-teal) 65%, rgba(159,212,196,0) 100%),
      radial-gradient(circle at 80% 60%, var(--sky-light) 0%, var(--sky-deep) 55%);
  }
  .hero-art::after {
    content: ""; position: absolute; left: 0; right: 0; bottom: 0; height: 24px;
    background: linear-gradient(to bottom, rgba(255,255,255,0) 0%, var(--white) 80%);
  }
  .intro {
    position: absolute; top: 1060px; left: 97px; width: 1060px;
    font-weight: 400; font-size: 47px; line-height: 57px; color: var(--ink-soft);
  }
  .results {
    position: absolute; top: 1317px; left: 0; width: 1200px; height: 1090px;
    background: var(--sun-yellow);
  }
  .virus-icon { position: absolute; border-radius: 50%; }
  .virus-icon.orange { left: 588px; top: 38px; width: 110px; height: 110px; background: var(--virus-orange); }
  .virus-icon.sage { left: 979px; top: 235px; width: 142px; height: 142px; background: var(--virus-sage); }

  .week-label { position: absolute; left: 244px; top: 78px; display: flex; align-items: baseline; }
  .week-label .word { font-size: 40px; font-weight: 400; }
  .week-label .number { font-size: 112px; font-weight: 800; font-style: italic; margin-left: 28px; line-height: 1; }
  .survey-note {
    position: absolute; left: 242px; top: 192px; width: 800px;
    font-size: 33px; line-height: 39px; font-weight: 400;
  }

  .stats-table { position: absolute; left: 97px; top: 365px; width: 1005px; z-index: 1; }
  .stats-head {
    height: 83px; background: var(--white); border-bottom: 5px solid var(--divider);
    display: flex; align-items: center; justify-content: center;
    font-size: 47px; font-weight: 900; color: #333;
  }
  .stats-body {
    margin-top: 14px; height: 565px; background: var(--white);
    display: grid; grid-template-columns: 376px 412px 1fr; grid-template-rows: repeat(4, 1fr);
  }
  .stats-body > div { display: flex; align-items: center; }
  .cell-bar { border-right: 3px solid var(--divider); padding-left: 28px; }
  .cell-label {
    border-right: 3px solid var(--divider); padding-left: 38px;
    font-family: "Arimo", sans-serif; font-size: 29.5px; line-height: 27px; color: var(--ink);
  }
  .cell-value { justify-content: center; font-size: 47px; font-weight: 900; }
  .red { color: var(--red); } .green { color: var(--green); }
  .indigo { color: var(--indigo); } .steel { color: var(--steel); }
  .bar { display: block; }
</style>
</head>
<body>
  <h1 class="page-title">Based on a survey of 400 U.S. adults.</h1>

  <div class="hero-art" role="img" aria-label="Illustration: a giant red-orange coronavirus chained like a ball and chain to a person wearing a U.S. flag face mask, against a blue sky"></div>

  <p class="intro">Everywhere you look there are messages about COVID. That is leading many people to feel fatigued and overloaded by the messages.</p>

  <section class="results">
    <div class="virus-icon orange" role="img" aria-label="Small orange virus icon"></div>
    <div class="virus-icon sage" role="img" aria-label="Small pale green virus icon"></div>

    <div class="week-label"><span class="word">WEEK:</span><span class="number">1</span></div>
    <p class="survey-note">Based on a survey of 400 U.S. adults conducted March 20 - 24th, 2020.</p>

    <div class="stats-table">
      <div class="stats-head">When it comes to coronavirus . . .</div>
      <div class="stats-body">
        <div class="cell-bar">
          <svg class="bar" width="322" height="20" viewBox="0 0 322 20" aria-hidden="true">
            <defs>
              <clipPath id="bar-segments">
                <rect x="0" y="0" width="29.5" height="20" rx="6"/>
                <rect x="32.5" y="0" width="29.5" height="20" rx="3"/>
                <rect x="65" y="0" width="29.5" height="20" rx="3"/>
                <rect x="97.5" y="0" width="29.5" height="20" rx="3"/>
                <rect x="130" y="0" width="29.5" height="20" rx="3"/>
                <rect x="162.5" y="0" width="29.5" height="20" rx="3"/>
                <rect x="195" y="0" width="29.5" height="20" rx="3"/>
                <rect x="227.5" y="0" width="29.5" height="20" rx="3"/>
                <rect x="260" y="0" width="29.5" height="20" rx="3"/>
                <rect x="292.5" y="0" width="29.5" height="20" rx="6"/>
              </clipPath>
            </defs>
            <g clip-path="url(#bar-segments)">
              <rect width="322" height="20" fill="var(--bar-empty)"/>
              <rect width="177" height="20" fill="var(--red)"/>
            </g>
          </svg>
        </div>
        <div class="cell-label">Feel exhausted by<br>all the messages.</div>
        <div class="cell-value red">55%</div>

        <div class="cell-bar">
          <svg class="bar" width="322" height="20" viewBox="0 0 322 20" aria-hidden="true">
            <g clip-path="url(#bar-segments)">
              <rect width="322" height="20" fill="var(--bar-empty)"/>
              <rect width="177" height="20" fill="var(--green)"/>
            </g>
          </svg>
        </div>
        <div class="cell-label">Feel overloaded by the<br>amount of information.</div>
        <div class="cell-value green">54%</div>

        <div class="cell-bar">
          <svg class="bar" width="322" height="20" viewBox="0 0 322 20" aria-hidden="true">
            <g clip-path="url(#bar-segments)">
              <rect width="322" height="20" fill="var(--bar-empty)"/>
              <rect width="161" height="20" fill="var(--indigo)"/>
            </g>
          </svg>
        </div>
        <div class="cell-label">Feel that the messages<br>are repetitive.</div>
        <div class="cell-value indigo">51%</div>

        <div class="cell-bar">
          <svg class="bar" width="322" height="20" viewBox="0 0 322 20" aria-hidden="true">
            <g clip-path="url(#bar-segments)">
              <rect width="322" height="20" fill="var(--bar-empty)"/>
              <rect width="152" height="20" fill="var(--steel)"/>
            </g>
          </svg>
        </div>
        <div class="cell-label">Feel like messages<br>exaggerate how bad it is.</div>
        <div class="cell-value steel">47%</div>
      </div>
    </div>
  </section>
</body>
</html>
```